New Website for Crime Scene Cleaner required

I need someone to create a complete new website and can set up SEO for me through the Website Designer or a third party for me. I have Logo that i will upload shortly once finalized for the website. I have domain names already but will need to be registered by the winner(i can supply the details I have received from NetHarbor). I am looking for a website that stands out but is simple and elegant, easy to navigate and use yet not boring. Using information provided by me for wording to create it as a stand out website. in total i am looking at 5-7 pages (About/Home, Fire & Smoke Restoration, Water Restoration/Mould Remediation, Crime Scene Cleaners, Methamphetamine Remediation/ Testing Services, Hoarding & Squalor Cleaning, Contact Us/Testimonials)This will be a start to finish project. I would like assistance to have it set up user friendly on mobile devices etc or refer a third party who can assist. Must be able to provide ongoing support when required by myself if the successful winner (i understand this will be an additional fee if required in the future).
You will also require to assist me with the email set up for the website so that it is fully functional or provide a third party who can.
To gain some information about the business you can visit my old website at www.pelgrosvandree.com.au and welcome to use some of the wording from there for your entry.
It's been 14yrs since i've had a website made from me so suggestions are welcome if not mentioned in the scope as I want the website to be great.

I have uploaded 2 Logo's and a 3D Logo will come through shortly.

Target Market(s)

People affected by a traumatic event in their lives needing assistance by professionals who are understanding and professionally trained

Coding

Coded - Design and coding required

Requirements
Must have
• *** Please note that correct wording for pages will only be supplied upon a successful winner for the finalization of the project.

I have domain names already but will need to be registered by the winner(i can supply the details I have received from NetHarbor).
Nice to have
• the feeling that we care because we do and that we are passionate for what we do.

```html
<!DOCTYPE html>
<html lang="en">
<head>
<meta charset="utf-8">
<title>Clearhaven Restore Services</title>
<link href="https://fonts.googleapis.com/css2?family=Bebas+Neue&family=Montserrat:wght@200;300;400;500;600&display=swap" rel="stylesheet">
<style>
:root{
  --orange:#f26a21;
  --orange-light:#f7901e;
  --orange-deep:#ec4b24;
  --ink:#2b2b2b;
  --muted:#6b6b6b;
  --blush:#fdeee8;
  --dark:#1f1f1f;
  --white:#ffffff;
}
*{margin:0;padding:0;box-sizing:border-box}
html,body{width:1200px;height:3394px;overflow:hidden}
body{position:relative;font-family:"Montserrat",sans-serif;color:var(--ink);background:var(--white)}
.abs{position:absolute}
.grad{background:linear-gradient(90deg,var(--orange-light),var(--orange-deep))}

/* top bar */
.topbar{left:0;top:0;width:1200px;height:37px}
.topnav{left:463px;top:11px;display:flex;gap:20px;font-size:11px;color:var(--white)}
.topnav span:first-child{color:var(--ink)}
.topphone{left:905px;top:8px;display:flex;align-items:center;gap:8px;color:var(--white);font-size:16px;font-weight:500}
.header{left:0;top:37px;width:1200px;height:80px;background:var(--white)}
.brand{left:160px;top:70px;display:flex;align-items:center;gap:6px;color:var(--orange);font-size:12px;font-weight:600;white-space:nowrap}
.brand i{width:20px;height:20px;border-radius:50%;background:var(--orange);display:block;flex:none}
.mainnav{left:356px;top:72px;display:flex;gap:18px;font-size:11.5px;color:var(--ink);white-space:nowrap}

/* hero */
.hero{left:0;top:117px;width:1200px;height:620px;overflow:hidden}
.hero-photo{position:absolute;inset:0;background:linear-gradient(100deg,#6e6e6e 0%,#3a3a3a 35%,#2a2624 65%,#1c1a19 100%)}
.hero-flame{position:absolute;right:0;top:220px;width:120px;height:260px;border-radius:60% 0 0 60%;background:radial-gradient(circle at 70% 60%,#f7901e,#e8441f 70%)}
.hero-curve{position:absolute;left:0;top:0}
.hero-tag{left:650px;top:252px;font-size:34px;font-weight:200;color:var(--orange-light)}
.hero-tag b{font-weight:600}
.hero-title{left:650px;top:305px;font-family:"Bebas Neue",sans-serif;font-size:58px;line-height:60px;color:var(--white);letter-spacing:.5px;font-weight:400}
.btn{display:flex;align-items:center;justify-content:space-between;padding:0 5px 0 22px;border-radius:22px;color:var(--white);font-size:15px;font-weight:500}
.btn .arr{width:30px;height:30px;border-radius:50%;background:var(--white);display:flex;align-items:center;justify-content:center}
.hero-btn{left:648px;top:442px;width:172px;height:40px}

/* about */
.about-photo{left:226px;top:816px;width:338px;height:338px;border-radius:50%;background:radial-gradient(circle at 40% 40%,#e7e7e7,#9a9a92 70%,#6e6d66)}
.years{left:342px;top:932px;width:106px;height:106px;border-radius:50%;border:8px solid var(--white);display:flex;flex-direction:column;align-items:center;justify-content:center;color:var(--white)}
.years b{font-size:48px;line-height:44px;font-weight:600}
.years span{font-size:15px;font-weight:500}
.eyebrow{font-size:14px;color:var(--ink)}
.about-eyebrow{left:639px;top:838px}
.section-title{font-size:36px;font-weight:500;color:var(--orange);letter-spacing:.5px}
.about-title{left:636px;top:860px;white-space:nowrap}
.about-copy{left:639px;top:914px;width:350px;font-size:11.5px;line-height:19.5px;color:var(--muted)}
.about-copy p+p{margin-top:11px}
.about-btn{left:639px;top:1080px;width:172px;height:41px}

/* services */
.services-bg{left:0;top:1140px;width:1200px;height:1000px}
.center{width:1200px;left:0;text-align:center}
.svc-eyebrow{top:1310px}
.svc-title{top:1334px}
.svc-copy{top:1384px;font-size:12px;line-height:21px;color:var(--muted)}
.card{width:246px;height:240px;background:var(--white);border-radius:4px;box-shadow:0 2px 8px rgba(0,0,0,.05);padding:5px}
.card .img{height:169px;width:100%}
.card p{text-align:center;font-size:14px;font-weight:500;line-height:18px;margin-top:20px;color:var(--ink)}
.card.active{background:linear-gradient(180deg,#f7901e,#ec4b24)}
.card.active p{color:var(--white)}
.emerg-title{left:773px;top:1813px;font-size:20px;font-weight:500}
.emerg-icon{left:773px;top:1858px}
.emerg-label{left:834px;top:1857px;font-size:12px;color:var(--orange)}
.emerg-num{left:830px;top:1872px;font-size:24px;font-weight:500;color:var(--orange)}

/* availability band */
.band{left:0;top:1990px;width:1200px;height:381px}
.band-person{left:665px;top:1995px;width:330px;height:376px;border-radius:160px 160px 0 0;background:linear-gradient(180deg,#e9e4e0,#cfc9c4)}
.band-title{left:272px;top:2148px;font-size:40px;font-weight:500;color:var(--white);white-space:nowrap}
.band-sub{left:272px;top:2200px;font-size:21px;line-height:29px;font-weight:400;color:var(--white);width:380px}
.band-btn{left:271px;top:2275px;width:173px;height:39px;border:1.5px solid var(--white)}

/* testimonials */
.t-eyebrow{top:2447px}
.t-title{top:2470px}
.t-quote{top:2528px;font-family:Georgia,serif;font-size:64px;line-height:60px;color:#36384a}
.t-copy{left:337px;top:2596px;width:526px;text-align:center;font-size:12px;line-height:22.5px;color:var(--muted)}
.t-arrow{top:2622px;width:38px;height:38px;background:var(--white);box-shadow:0 2px 8px rgba(0,0,0,.12);display:flex;align-items:center;justify-content:center}
.avatar{border-radius:50%;border:3px solid var(--white);box-shadow:0 2px 6px rgba(0,0,0,.15)}
.t-name{top:2816px;font-size:13.5px;font-weight:500;color:var(--orange);z-index:2}
.t-role{top:2840px;font-size:11px;color:var(--ink);z-index:2}

/* footer */
.footer-bg{left:0;top:2862px;width:1200px;height:490px;background:linear-gradient(180deg,#2a2a2a,#1b1b1b 60%,#262626)}
.footer-wave{left:0;top:2862px}
.f-title{left:162px;top:2994px;font-size:28px;font-weight:500;color:var(--orange)}
.f-sub{left:162px;top:3033px;font-size:13px;color:var(--white)}
.field{height:35px;background:#3b3b3b;border:1px solid #4a4a4a;color:#a8a8a8;font-size:10.5px;padding:10px 11px}
.submit{left:161px;top:3251px;width:130px;height:39px}
.f-head{top:3014px;font-size:15px;font-weight:500;color:var(--orange)}
.links{left:601px;top:3066px;list-style:none;font-size:11px;color:#c9c9c9}
.links li{height:22.4px;display:flex;align-items:center;gap:11px}
.links li:before{content:"";width:4px;height:4px;border-radius:50%;background:var(--orange)}
.info{left:863px;font-size:11px;line-height:18px;color:#d8d8d8}
.info.small{font-size:10px}
.info-icon{left:828px}
.social{left:822px;top:3240px;width:34px;height:34px;border-radius:50%;background:var(--orange)}
.copyright{left:0;top:3348px;width:1200px;height:46px;display:flex;align-items:center;justify-content:center;font-size:10px;color:var(--white)}
</style>
</head>
<body>

<!-- top bar -->
<div class="abs topbar grad"></div>
<nav class="abs topnav"><span>Home</span><span>About Us</span><span>Testimonials</span><span>Contact Us</span></nav>
<div class="abs topphone">
  <svg width="20" height="20" viewBox="0 0 24 24" fill="none" stroke="#fff" stroke-width="1.6"><path d="M5 3h4l2 5-2.5 1.5a11 11 0 0 0 6 6L16 13l5 2v4a2 2 0 0 1-2 2A17 17 0 0 1 3 5a2 2 0 0 1 2-2z"/></svg>
  0491 570 156
</div>
<header class="abs header"></header>
<div class="abs brand"><i></i>CLEARHAVEN RESTORE</div>
<nav class="abs mainnav"><span>Fire &amp; Smoke Restoration</span><span>Water Restoration</span><span>Crime Scene Cleaners</span><span>Testing Services</span><span>Hoarding &amp; Squalor Cleaning</span></nav>

<!-- hero -->
<section class="abs hero">
  <div class="hero-photo" role="img" aria-label="Technician in protective suit and mask behind crime scene tape in a dark stairwell"></div>
  <div class="hero-flame" role="img" aria-label="Orange flame illustration"></div>
  <svg class="hero-curve" width="1200" height="620" viewBox="0 0 1200 620">
    <defs><linearGradient id="heroSwoosh" x1="0" x2="1"><stop offset="0" stop-color="#f7901e"/><stop offset="1" stop-color="#ec4b24"/></linearGradient></defs>
    <path d="M0 440 C180 560 420 630 760 580 C960 550 1100 500 1200 470 L1200 620 L0 620Z" fill="url(#heroSwoosh)"/>
    <path d="M0 560 C200 640 520 640 820 600 C1000 570 1120 510 1200 478 L1200 620 L0 620Z" fill="#fff"/>
  </svg>
</section>
<div class="abs hero-tag">We're Here To <b>Help.</b></div>
<h1 class="abs hero-title">24/7 CRIME SCENE &amp;<br>HOME CLEANUP</h1>
<div class="abs btn grad hero-btn">CONTACT US<span class="arr"><svg width="16" height="16" viewBox="0 0 16 16" fill="none" stroke="#f26a21" stroke-width="2"><path d="M2 8h11M9 4l4 4-4 4"/></svg></span></div>

<!-- about -->
<div class="abs about-photo" role="img" aria-label="Technician in respirator spraying mould on a wall"></div>
<div class="abs years grad"><b>14</b><span>Years</span></div>
<div class="abs eyebrow about-eyebrow">Welcome To</div>
<h2 class="abs section-title about-title">CLEARHAVEN RESTORE</h2>
<div class="abs about-copy">
  <p>Lorem Ipsum is simply dummy text of the printing typesetti industry. Lorem Ipsum has been the industry's standard dummy text ever since the when.</p>
  <p>Lorem Ipsum is simply dummy text of the printing typesetti industry. Lorem Ipsum has been the industry's standard dummy text ever since the 1500s, when an unknown printer took a the galley of type and scrambled it to.</p>
</div>
<div class="abs btn grad about-btn">KNOW MORE<span class="arr"><svg width="16" height="16" viewBox="0 0 16 16" fill="none" stroke="#f26a21" stroke-width="2"><path d="M2 8h11M9 4l4 4-4 4"/></svg></span></div>

<!-- services -->
<svg class="abs services-bg" width="1200" height="1000" viewBox="0 0 1200 1000">
  <defs><linearGradient id="blush" x1="0" x2="1"><stop offset="0" stop-color="#fdf1ea"/><stop offset="1" stop-color="#fde7e3"/></linearGradient></defs>
  <path d="M0 0 C300 110 700 120 1200 20 L1200 1000 L0 1000Z" fill="url(#blush)"/>
</svg>
<div class="abs center eyebrow svc-eyebrow">What We Do</div>
<h2 class="abs center section-title svc-title">SERVICES WE PROVIDE</h2>
<p class="abs center svc-copy">Lorem Ipsum is simply dummy text of the printing typesetti industry the<br>Lorem Ipsum has been the industry.</p>

<div class="abs card active" style="left:207px;top:1462px"><div class="img" role="img" aria-label="House on fire with firefighter" style="background:linear-gradient(160deg,#b9c3c8,#8a6a3a 55%,#4f6a3c)"></div><p>Fire &amp; Smoke<br>Restoration</p></div>
<div class="abs card" style="left:477px;top:1462px"><div class="img" role="img" aria-label="Worker in protective suit treating mould" style="background:linear-gradient(160deg,#e4e1dc,#b4aea3 60%,#7c776c)"></div><p>Water Restoration/Mould<br>Remediation</p></div>
<div class="abs card" style="left:747px;top:1462px"><div class="img" role="img" aria-label="Gloved hand holding police tape" style="background:linear-gradient(160deg,#1c2a44,#3f5e8e 50%,#d4b52a)"></div><p>Crime Scene<br>Cleaners</p></div>
<div class="abs card" style="left:207px;top:1729px"><div class="img" role="img" aria-label="Gloved hand holding a bag of crystals" style="background:linear-gradient(160deg,#0f0f0f,#2d3a56 55%,#cfcfd6)"></div><p>Methamphetamine<br>Remediation/ Testing Services</p></div>
<div class="abs card" style="left:477px;top:1729px"><div class="img" role="img" aria-label="Cluttered hoarded room" style="background:linear-gradient(160deg,#8b5a45,#5a4638 55%,#a98f6d)"></div><p>Hoarding &amp;<br>Squalor Cleaning</p></div>

<div class="abs emerg-title">Have Emergency ?</div>
<svg class="abs emerg-icon" width="46" height="38" viewBox="0 0 46 38"><path d="M3 12c0-6 40-6 40 0v4h-9v-4c-7-2-15-2-22 0v4H3z" fill="#2b2b2b"/><path d="M9 18h28l4 18H5z" fill="#2b2b2b"/><circle cx="23" cy="27" r="6" fill="#f26a21"/></svg>
<div class="abs emerg-label">Call Us On :</div>
<div class="abs emerg-num">0491 570 156</div>

<!-- availability band -->
<svg class="abs band" width="1200" height="381" viewBox="0 0 1200 381">
  <defs><linearGradient id="bandGrad" x1="0" x2="1"><stop offset="0" stop-color="#f7901e"/><stop offset="1" stop-color="#ec4b24"/></linearGradient></defs>
  <path d="M0 130 C250 60 550 20 850 10 C1000 8 1120 30 1200 60 L1200 381 L0 381Z" fill="url(#bandGrad)"/>
</svg>
<div class="abs band-person" role="img" aria-label="Smiling woman holding a smartphone"></div>
<h2 class="abs band-title">24/7 AVIALABLE</h2>
<p class="abs band-sub">Cleaning &amp; Property Maintenance<br>Specialist</p>
<div class="abs btn band-btn">CONTACT US<span class="arr"><svg width="16" height="16" viewBox="0 0 16 16" fill="none" stroke="#f26a21" stroke-width="2"><path d="M2 8h11M9 4l4 4-4 4"/></svg></span></div>

<!-- testimonials -->
<div class="abs center eyebrow t-eyebrow">Testimonials</div>
<h2 class="abs center section-title t-title">WHAT OUR CLIENT SAY</h2>
<div class="abs center t-quote">&ldquo;</div>
<p class="abs t-copy">" I have used Joris Van Dree cleaners for over a year now and I have always been more than happy with their work. They are professional, quick and fairly priced. I would recommend their team to anyone and have done so. Thanks to Joris Van Dree know that the property will be cleaned properly and I am confident they will do the same for you. Thank you. "</p>
<div class="abs t-arrow" style="left:179px"><svg width="12" height="12" viewBox="0 0 12 12" fill="none" stroke="#999" stroke-width="1.5"><path d="M8 1L3 6l5 5"/></svg></div>
<div class="abs t-arrow" style="left:973px"><svg width="12" height="12" viewBox="0 0 12 12" fill="none" stroke="#f26a21" stroke-width="1.5"><path d="M4 1l5 5-5 5"/></svg></div>
<div class="abs avatar" role="img" aria-label="Client portrait" style="left:503px;top:2736px;width:52px;height:52px;background:#b9cfe0"></div>
<div class="abs avatar" role="img" aria-label="Client portrait" style="left:565px;top:2727px;width:70px;height:70px;background:#6a4a35"></div>
<div class="abs avatar" role="img" aria-label="Client portrait" style="left:645px;top:2736px;width:52px;height:52px;background:#c9c4c0"></div>

<!-- footer -->
<div class="abs footer-bg" role="img" aria-label="Dim photo of hands cleaning a carpet"></div>
<svg class="abs footer-wave" width="1200" height="120" viewBox="0 0 1200 120"><path d="M0 0 L1200 0 L1200 40 C900 120 400 120 0 10Z" fill="#fff"/></svg>

<div class="abs center t-name">Clara Whitmore, Property Manager</div>
<div class="abs center t-role">Harbourline Property, Westvale</div>

<div class="abs f-title">Contact Us</div>
<div class="abs f-sub">If you have an any Question for contact us Today :</div>
<div class="abs field" style="left:162px;top:3071px;width:186px">Name *</div>
<div class="abs field" style="left:359px;top:3071px;width:187px">Email *</div>
<div class="abs field" style="left:162px;top:3116px;width:186px">Phone *</div>
<div class="abs field" style="left:359px;top:3116px;width:187px">Services *</div>
<svg class="abs" style="left:526px;top:3131px" width="8" height="5" viewBox="0 0 8 5"><path d="M0 0h8L4 5z" fill="#ccc"/></svg>
<div class="abs field" style="left:162px;top:3161px;width:384px;height:75px">Inquiry*</div>
<div class="abs btn grad submit">SUBMIT<span class="arr"><svg width="16" height="16" viewBox="0 0 16 16" fill="none" stroke="#f26a21" stroke-width="2"><path d="M2 8h11M9 4l4 4-4 4"/></svg></span></div>

<div class="abs f-head" style="left:601px">QuickLinks</div>
<ul class="abs links">
  <li>Home</li><li>About Us</li><li>Fire &amp; Smoke Restoration</li><li>Water Restoration</li><li>Crime Scene Cleaners</li><li>Testing Services</li><li>Hoarding &amp; Squalor Cleaning</li><li>Testimonials</li><li>Contact Us</li>
</ul>

<div class="abs f-head" style="left:830px">Contact Info</div>
<svg class="abs info-icon" style="top:3070px" width="16" height="22" viewBox="0 0 16 22"><path d="M8 1a7 7 0 0 1 7 7c0 5-7 13-7 13S1 13 1 8a7 7 0 0 1 7-7z" fill="none" stroke="#f26a21" stroke-width="1.6"/><circle cx="8" cy="8" r="2.5" fill="#f26a21"/></svg>
<div class="abs info small" style="top:3067px">12 Ridge Lane<br>Springfield QLD 4300</div>
<svg class="abs info-icon" style="top:3121px" width="17" height="12" viewBox="0 0 17 12"><rect width="17" height="12" rx="1" fill="#f26a21"/><path d="M1 1l7.5 6L16 1" fill="none" stroke="#262626" stroke-width="1.2"/></svg>
<div class="abs info" style="top:3117px">inquiries@pelgrosvandree.com.au</div>
<svg class="abs info-icon" style="top:3157px" width="17" height="17" viewBox="0 0 24 24"><path d="M5 2h4l2 5-2.5 1.5a11 11 0 0 0 6 6L16 12l5 2v4a2 2 0 0 1-2 2A17 17 0 0 1 3 4a2 2 0 0 1 2-2z" fill="#f26a21"/></svg>
<div class="abs info" style="top:3156px;font-size:12px">0491 570 156</div>
<svg class="abs info-icon" style="top:3202px" width="17" height="17" viewBox="0 0 24 24"><path d="M5 2h4l2 5-2.5 1.5a11 11 0 0 0 6 6L16 12l5 2v4a2 2 0 0 1-2 2A17 17 0 0 1 3 4a2 2 0 0 1 2-2z" fill="#f26a21"/></svg>
<div class="abs info small" style="top:3193px;color:#a8a8a8">Emergency and After Hours</div>
<div class="abs info" style="top:3213px;font-size:12px">0491 570 156</div>
<div class="abs social"></div>

<div class="abs copyright grad">©CLEARHAVEN RESTORE SERVICES - 2020 All rights reserved.</div>

</body>
</html>
```